Brick lantern real estate investment company needs a poster design

We would like a poster design size 18 x 24.
Poster wording -
I WANT TO BUY YOUR ( finish with logo) logo uploaded
website- www.bricklantern.example
phone # 555-817-2643 ( color red for the phone number)
we would like to see the poster on 2 different backgrounds
Yellow background
White background
horizontal

```html
<!DOCTYPE html>
<html lang="en">
<head>
<meta charset="utf-8">
<title>Brick Lantern – Yard Sign Poster</title>
<link rel="stylesheet" href="https://fonts.googleapis.com/css2?family=Luckiest+Guy&family=Roboto+Condensed:wght@700&display=swap">
<style>
  :root {
    --stage: #9a9a9a;
    --sign-yellow: #ffdd15;
    --sign-white: #ffffff;
    --ink: #231f20;
    --accent-red: #ee1c2e;
    --band-text: #ffffff;
  }
  * { box-sizing: border-box; margin: 0; padding: 0; }
  html, body { width: 1200px; height: 683px; overflow: hidden; }
  body { background: var(--stage); position: relative; }

  .sign {
    position: absolute;
    top: 179px;
    width: 423px;
    height: 316px;
  }
  .sign--yellow { left: 163px; background: var(--sign-yellow); }
  .sign--white  { left: 605px; background: var(--sign-white); }

  .roof {
    position: absolute;
    left: 0; top: 0;
    width: 423px; height: 316px;
  }
  .roof polygon { fill: var(--ink); }

  .headline {
    position: absolute;
    left: 0; right: 0;
    text-align: center;
    font-family: "Luckiest Guy", "Arial Black", sans-serif;
    line-height: 1;
    white-space: nowrap;
  }
  .headline--want  { top: 82px;  font-size: 44px; color: var(--accent-red); }
  .headline--buy   { top: 138px; font-size: 42px; color: var(--ink); }
  .headline--brand { top: 196px; font-size: 44px; color: var(--ink); letter-spacing: 1px; }

  .contact-band {
    position: absolute;
    left: 26px; top: 258px;
    width: 372px; height: 45px;
    background: var(--ink);
    display: flex;
    align-items: center;
    justify-content: center;
    gap: 7px;
    font-family: "Roboto Condensed", "Arial Narrow", sans-serif;
    font-weight: 700;
    font-size: 18px;
    color: var(--band-text);
    white-space: nowrap;
  }
  .contact-band .divider {
    width: 6px; height: 6px; border-radius: 50%;
  }
  .sign--yellow .divider { background: var(--sign-yellow); }
  .sign--white .divider  { background: var(--accent-red); }
</style>
</head>
<body>

  <section class="sign sign--yellow">
    <svg class="roof" viewBox="0 0 320 239" aria-hidden="true">
      <polygon points="20,90 161,10 301,90 301,119 161,41 20,119"/>
    </svg>
    <p class="headline headline--want">I WANT</p>
    <p class="headline headline--buy">TO BUY YOUR</p>
    <p class="headline headline--brand">BRICK LANTERN</p>
    <div class="contact-band">
      <span class="website">www.bricklantern.example</span>
      <span class="divider"></span>
      <span class="phone">555-817-2643</span>
    </div>
  </section>

  <section class="sign sign--white">
    <svg class="roof" viewBox="0 0 320 239" aria-hidden="true">
      <polygon points="20,90 161,10 301,90 301,119 161,41 20,119"/>
    </svg>
    <p class="headline headline--want">I WANT</p>
    <p class="headline headline--buy">TO BUY YOUR</p>
    <p class="headline headline--brand">BRICK LANTERN</p>
    <div class="contact-band">
      <span class="website">www.bricklantern.example</span>
      <span class="divider"></span>
      <span class="phone">555-817-2643</span>
    </div>
  </section>

</body>
</html>
```